Business Card for Inovative Flexible Packaging Company

Create a business card that is both simple and stricking at the same time.
Preferably only one color (orange) or two colors (black and orange).
Information to print:
Torvalo, Lda
[T] 22 418 6093
[M] 91 326 7041
[F] 22 418 6135
[@] torvalo.ac@correiomx.com
SEDE & ARMAZÉM
Rua Das Figueiras do Monte, 312
Lavrinhas
4590-832 Lavrinhas - Vila Serrana
PORTUGAL
Reason: A lot of the ideas are obvious. I want something different. Inovative. dare to do something eye catching with style.
Business Consumers. Packaging Designers.
Business

```html
<!DOCTYPE html>
<html lang="pt">
<head>
<meta charset="utf-8">
<title>Torvalo, Lda — Business Card</title>
<link rel="stylesheet" href="https://fonts.googleapis.com/css2?family=Montserrat:wght@700&family=Questrial&display=swap">
<style>
  :root {
    --orange: #f26a0f;
    --peach: #fbd9bf;
    --peach-soft: #fff3ea;
    --ink: #2b2b2b;
    --muted: #6b6b6b;
    --white: #ffffff;
    --black: #0b0b0b;
    --backdrop: #d9d6d2;
  }
  * { box-sizing: border-box; margin: 0; padding: 0; }
  html, body { width: 1200px; height: 675px; overflow: hidden; }
  body {
    background: var(--backdrop);
    font-family: "Questrial", sans-serif;
    display: flex;
    align-items: center;
    justify-content: center;
    gap: 40px;
  }
  .card {
    position: relative;
    width: 540px;
    height: 309px;
    overflow: hidden;
    box-shadow: 0 10px 30px rgba(0,0,0,0.18);
  }

  /* Front */
  .card--front { background: var(--white); color: var(--ink); }
  .front__wash {
    position: absolute;
    left: 0; top: 0;
    width: 250px; height: 100%;
    background: linear-gradient(100deg, var(--peach) 0%, var(--peach-soft) 70%, var(--white) 100%);
  }
  .brand {
    position: absolute;
    left: 40px; top: 72px;
  }
  .brand__row { display: flex; align-items: center; gap: 12px; }
  .brand__square {
    width: 26px; height: 26px;
    background: var(--orange);
  }
  .brand__name {
    font-family: "Questrial", sans-serif;
    font-size: 38px;
    line-height: 1;
    color: var(--orange);
  }
  .brand__tagline {
    margin-top: 8px;
    margin-left: 38px;
    font-size: 8px;
    letter-spacing: 2.6px;
    color: var(--muted);
  }
  .contacts {
    position: absolute;
    left: 48px; top: 178px;
    list-style: none;
    font-size: 13px;
    line-height: 1;
  }
  .contacts li { display: flex; align-items: center; gap: 12px; margin-bottom: 9px; }
  .contacts svg { width: 13px; height: 13px; fill: var(--orange); flex: none; }

  .company {
    position: absolute;
    right: 40px; top: 40px;
    font-family: "Montserrat", sans-serif;
    font-weight: 700;
    font-size: 15px;
    color: var(--orange);
  }
  .address {
    position: absolute;
    right: 40px; top: 150px;
    text-align: right;
    font-style: normal;
    font-size: 12.5px;
    line-height: 1.45;
  }
  .address__title {
    font-family: "Montserrat", sans-serif;
    font-weight: 700;
    font-size: 10px;
    color: var(--orange);
    letter-spacing: 0.3px;
    margin-bottom: 2px;
  }

  /* Back */
  .card--back {
    background: var(--black);
    display: flex;
    flex-direction: column;
    align-items: center;
    justify-content: center;
  }
  .card--back .brand { position: static; }
  .card--back .brand__square { width: 40px; height: 40px; }
  .card--back .brand__name { font-size: 58px; }
  .card--back .brand__tagline {
    color: var(--white);
    font-size: 11px;
    letter-spacing: 4.5px;
    margin-left: 52px;
    margin-top: 10px;
  }
</style>
</head>
<body>

  <section class="card card--front" aria-label="Card front">
    <div class="front__wash"></div>

    <div class="brand">
      <div class="brand__row">
        <span class="brand__square"></span>
        <span class="brand__name">Torvalo</span>
      </div>
      <p class="brand__tagline">ADAPTIVE WRAP SYSTEMS</p>
    </div>

    <ul class="contacts">
      <li>
        <svg viewBox="0 0 16 16" aria-label="Telefone"><path d="M3 1l3 3-1.5 2a9 9 0 0 0 5.5 5.5L12 10l3 3-2 2C6 15 1 10 1 3z"/></svg>
        <span>22 418 6093</span>
      </li>
      <li>
        <svg viewBox="0 0 16 16" aria-label="Telemóvel"><path d="M4 0h8a1 1 0 0 1 1 1v14a1 1 0 0 1-1 1H4a1 1 0 0 1-1-1V1a1 1 0 0 1 1-1zm1 2v10h6V2zm3 11a1 1 0 1 0 0 2 1 1 0 0 0 0-2z"/></svg>
        <span>91 326 7041</span>
      </li>
      <li>
        <svg viewBox="0 0 16 16" aria-label="Fax"><path d="M4 0h6l2 2v4H4zM1 7h14v6h-3v3H4v-3H1zm4 5v2h6v-2z"/></svg>
        <span>22 418 6135</span>
      </li>
      <li>
        <svg viewBox="0 0 16 16" aria-label="Email"><path d="M0 3h16v10H0zm1.5 1.2V5l6.5 4 6.5-4v-.8z"/></svg>
        <span>torvalo.ac@correiomx.com</span>
      </li>
    </ul>

    <p class="company">Torvalo, Lda</p>

    <address class="address">
      <p class="address__title">SEDE &amp; ARMAZÉM</p>
      <p>Rua Das Figueiras do Monte, 312</p>
      <p>Lavrinhas</p>
      <p>4590-832 Lavrinhas - Vila Serrana</p>
      <p>PORTUGAL</p>
    </address>
  </section>

  <section class="card card--back" aria-label="Card back">
    <div class="brand">
      <div class="brand__row">
        <span class="brand__square"></span>
        <span class="brand__name">Torvalo</span>
      </div>
      <p class="brand__tagline">ADAPTIVE WRAP SYSTEMS</p>
    </div>
  </section>

</body>
</html>
```